The Kestrel Personal Training Studio Information Card

The front and back of card to give people that walk in to our gym. There are a few things to say on the card. But it also needs to be designed in an attractive way. You can make some of the information bullett points or with icons or graphics. Please look at our website at https://thekestrelfitness-example.com/ . The card will be 4" x 9"

Target Market(s)

High End Clientele who want to train in a private gym

Industry/Entity Type

Fitness

Font styles to use
Serif
Sans Serif
Other font styles liked:
• the same font Vorlex uses on the zuntab

Colors
F0912C
F2A743
F7CA91
FBE8D2
FDF5EE

Requirements
Must have
• A cool look

```html
<!DOCTYPE html>
<html lang="en">
<head>
<meta charset="utf-8">
<title>The Kestrel Personal Training Studio – Information Card</title>
<link rel="stylesheet" href="https://fonts.googleapis.com/css2?family=Jost:wght@500;700&family=Arimo:ital,wght@0,400;1,400&display=swap">
<style>
  :root {
    --header-bg: #3a3a3c;
    --panel-dark: #1c1c1d;
    --panel-mid: #2e2e2f;
    --photo-light: #4b4a48;
    --photo-warm: #5a4a3a;
    --accent: #e6411d;
    --text: #ffffff;
  }
  * { margin: 0; padding: 0; box-sizing: border-box; }
  html, body { width: 1200px; height: 2699px; overflow: hidden; background: var(--panel-dark); }
  .card { position: relative; width: 1200px; height: 2699px; overflow: hidden; font-family: "Arimo", Helvetica, Arial, sans-serif; color: var(--text); }

  .header { position: absolute; left: 0; top: 0; width: 1200px; height: 441px; background: var(--header-bg); }
  .brand { position: absolute; left: 0; top: 150px; width: 1200px; text-align: center; font-family: "Jost", sans-serif; font-weight: 700; color: var(--text); }
  .brand-name { display: block; font-size: 124px; line-height: 1; letter-spacing: 1px; text-transform: uppercase; }
  .brand-tag { display: block; margin-top: 26px; font-size: 25px; letter-spacing: 11px; text-transform: uppercase; }

  .backdrop { position: absolute; left: 0; top: 441px; width: 1200px; height: 2258px;
    background:
      radial-gradient(ellipse 520px 420px at 62% 17%, var(--photo-light) 0%, transparent 75%),
      radial-gradient(ellipse 300px 120px at 95% 17%, var(--photo-warm) 0%, transparent 80%),
      radial-gradient(ellipse 700px 500px at 45% 70%, #333 0%, transparent 70%),
      linear-gradient(180deg, var(--panel-mid) 0%, var(--panel-dark) 100%); }

  .headline { position: absolute; left: 120px; top: 552px; width: 1060px; font-family: "Jost", sans-serif; font-weight: 500; font-size: 121px; line-height: 135px; letter-spacing: -0.5px; }
  .intro { position: absolute; left: 122px; top: 1180px; width: 1040px; font-style: italic; font-size: 38.5px; line-height: 43.5px; }
  .body-copy { position: absolute; left: 122px; top: 1446px; width: 1040px; font-size: 38.5px; line-height: 54px; }

  .goal-icon { position: absolute; fill: var(--accent); }
  .goal-label { position: absolute; font-size: 43px; line-height: 53px; }
</style>
</head>
<body>
<main class="card">
  <header class="header">
    <div class="brand">
      <span class="brand-name">The Kestrel</span>
      <span class="brand-tag">Personal Training Studio</span>
    </div>
  </header>

  <div class="backdrop" role="img" aria-label="Dark moody photo of gym weight plates and equipment"></div>

  <h1 class="headline">A Safe and<br>Individualized<br>Approach to<br>Strength Training.</h1>

  <p class="intro">Each of our clients have different goals: Build<br>strength, Increase Flexibility, Improve functional<br>movement, Train for a specific event, Weight Loss,<br>etc. We will tailor your training program according<br>to the results you wish to achieve.</p>

  <p class="body-copy">Some training practices increase the risk of<br>becoming injured. At The Kestrel our programs are<br>individually designed to help our clients get results<br>safely and effectively. Many of our clients are<br>dealing with pain from a former injury making it<br>very difficult for them to workout on their own. Our<br>trainers are skilled to work with people with these<br>problematic injuries allowing them to enjoy working<br>out again without pain while achieving their goals,<br>thus enhancing their quality of life.</p>

  <svg class="goal-icon" style="left:128px;top:2108px" width="104" height="96" viewBox="0 0 104 96" aria-hidden="true">
    <rect x="2" y="6" width="14" height="24" rx="3"/><rect x="88" y="6" width="14" height="24" rx="3"/>
    <rect x="14" y="14" width="76" height="8"/>
    <circle cx="52" cy="38" r="11"/>
    <path d="M40 50 h24 l-6 18 l16 22 h-14 l-12-16 l-12 16 h-14 l16-22 z"/>
  </svg>
  <div class="goal-label" style="left:279px;top:2118px">Build<br>strength</div>

  <svg class="goal-icon" style="left:690px;top:2110px" width="104" height="96" viewBox="0 0 104 96" aria-hidden="true">
    <circle cx="76" cy="18" r="16"/>
    <path d="M2 92 L58 46 Q80 30 88 56 L96 92 Z"/>
  </svg>
  <div class="goal-label" style="left:833px;top:2114px">Increase<br>Flexibility</div>

  <svg class="goal-icon" style="left:140px;top:2268px" width="50" height="104" viewBox="0 0 50 104" aria-hidden="true">
    <rect x="10" y="0" width="30" height="16" rx="3"/><rect x="10" y="88" width="30" height="16" rx="3"/>
    <rect x="0" y="12" width="50" height="80" rx="10"/>
    <rect x="10" y="40" width="30" height="24" rx="3" fill="#1c1c1d"/>
    <rect x="16" y="48" width="18" height="8" fill="#e6411d"/>
  </svg>
  <div class="goal-label" style="left:279px;top:2284px">Train for<br>an event</div>

  <svg class="goal-icon" style="left:662px;top:2272px" width="156" height="96" viewBox="0 0 156 96" aria-hidden="true">
    <path d="M14 24 v40 h-9 l13 18 l13-18 h-9 v-40 z" fill="none" stroke="#e6411d" stroke-width="4"/>
    <rect x="56" y="6" width="94" height="84" rx="14" fill="none" stroke="#e6411d" stroke-width="7"/>
    <rect x="70" y="20" width="66" height="26" rx="5" fill="none" stroke="#e6411d" stroke-width="4"/>
    <path d="M76 84 L90 60 h26 l14 24" fill="none" stroke="#e6411d" stroke-width="4"/>
  </svg>
  <div class="goal-label" style="left:846px;top:2280px">Weight<br>Loss</div>

  <svg class="goal-icon" style="left:320px;top:2456px" width="108" height="84" viewBox="0 0 108 84" aria-hidden="true">
    <circle cx="14" cy="40" r="13"/>
    <path d="M30 34 L72 4 L86 16 L62 40 L102 80 L82 82 L54 52 L38 82 L22 76 L40 42 Z"/>
  </svg>
  <div class="goal-label" style="left:471px;top:2462px">Improve functional<br>movement</div>
</main>
</body>
</html>
```